vantoreq realty business card

We need a Business card for our new business. The logo was designed by BrushQuill, and the text We want on the back is:
REAL ESTATE INVESTMENTS
- BUY, RENOVATE, SELL AND RENT RESIDENTIAL PROPERTIES
- FULL HOME REHABBING , REMODELING AND INTERIOR DESIGN
- HOME STAGING SERVICES
- WHOLESALE INVESTOR PROPERTIES
- MAKE CASH OFFERS ON HOUSES IN ANY CONDITION AND IN ANY SITUATION
- PRIVATE MONEY INVESTOR PROGRAMS WITH 6-12% RETURNS
- PAY CASH REWARDS FOR REFFERALS
- CONCIERGE SERVICE

Business

```html
<!DOCTYPE html>
<html lang="en">
<head>
<meta charset="utf-8">
<title>vantoreq realty business card</title>
<link rel="stylesheet" href="https://fonts.googleapis.com/css2?family=Exo+2:wght@400;500;600&display=swap">
<style>
:root{
  --bg:#2b2b2d;
  --teal:#8ecbd0;
  --teal-deep:#6fb6bd;
  --accent:#4fb3c0;
  --ink:#5d5e62;
  --ink-soft:#7b7c80;
  --paper:#ffffff;
  --paper-shade:#ececec;
  --band-grey:#6d6e72;
}
*{margin:0;padding:0;box-sizing:border-box}
html,body{width:1200px;height:900px;overflow:hidden}
body{background:var(--bg);font-family:"Exo 2",sans-serif;position:relative}
.card{position:absolute;left:280px;width:640px;height:366px;border-radius:26px;overflow:hidden}
.card-back{top:60px;background:linear-gradient(160deg,#9ed3d7 0%,var(--teal) 55%,var(--teal-deep) 100%)}
.card-front{top:474px;background:linear-gradient(170deg,var(--paper) 0%,var(--paper) 60%,var(--paper-shade) 100%)}

/* back */
.back-brand{position:absolute;left:30px;top:180px;width:310px;text-align:center;color:var(--paper)}
.brand-name{font-weight:500;font-size:28px;letter-spacing:.5px;display:flex;align-items:center;justify-content:center;gap:10px;white-space:nowrap}
.brand-mark{width:14px;height:14px;background:currentColor;display:inline-block;flex:none}
.brand-tagline{font-size:13px;letter-spacing:2.4px;margin-top:6px;opacity:.9}
.back-divider{position:absolute;left:360px;top:40px;width:1px;height:286px;background:rgba(255,255,255,.85)}
.services{position:absolute;left:382px;top:44px;width:236px;color:var(--paper);font-size:12.5px;line-height:1.3}
.services h2{font-size:12.5px;font-weight:600;letter-spacing:.4px;margin-bottom:4px}
.services ul{list-style:none}
.services li{margin-bottom:3px}
.services li::before{content:"- "}

/* front */
.front-brand{position:absolute;right:40px;top:40px;text-align:right;color:var(--accent)}
.front-brand .brand-name{justify-content:flex-end}
.front-brand .brand-tagline{color:var(--ink-soft);letter-spacing:2.2px}
.person{position:absolute;left:40px;top:188px}
.person-name{color:var(--accent);font-weight:600;font-size:17px;line-height:22px}
.person-role{color:var(--ink);font-size:16px;line-height:22px}
.front-rule{position:absolute;left:220px;right:40px;top:200px;height:1px;background:var(--ink-soft)}
.address{position:absolute;right:40px;top:212px;text-align:right;color:var(--ink);font-size:15px;line-height:1.4;font-style:normal}
.contact{position:absolute;left:40px;top:248px;list-style:none;color:var(--ink);font-size:17px}
.contact li{display:flex;align-items:center;gap:12px;height:26px}
.contact svg{width:16px;height:16px;fill:var(--accent);flex:none}
.front-bands{position:absolute;left:0;bottom:0;width:640px;height:44px}
</style>
</head>
<body>

<section class="card card-back" aria-label="Card back">
  <div class="back-brand">
    <div class="brand-name"><span class="brand-mark"></span>VANTOREQ Realty</div>
    <div class="brand-tagline">REAL ESTATE SOLUTIONS</div>
  </div>
  <div class="back-divider"></div>
  <div class="services">
    <h2>REAL ESTATE INVESTMENTS</h2>
    <ul>
      <li>Buy, Renovate, Sell And Rent Residential Properties</li>
      <li>Full Home Rehabbing, Remodeling And Interior Design</li>
      <li>Home Staging Services</li>
      <li>Wholesale Investor Properties</li>
      <li>Make Cash Offers On Houses In Any Condition And In Any Situation</li>
      <li>Private Money Investor Programs With 6-12% Returns</li>
      <li>Pay Cash Rewards For Refferals</li>
      <li>Concierge Service</li>
    </ul>
  </div>
</section>

<section class="card card-front" aria-label="Card front">
  <div class="front-brand">
    <div class="brand-name"><span class="brand-mark"></span>VANTOREQ Realty</div>
    <div class="brand-tagline">REAL ESTATE SOLUTIONS</div>
  </div>
  <div class="person">
    <div class="person-name">Marcus Elridge</div>
    <div class="person-role">managing director</div>
  </div>
  <div class="front-rule"></div>
  <address class="address">
    48 Linden Row<br>
    Brookvale, New York 12408<br>
    www.vantoreqrealty.com
  </address>
  <ul class="contact">
    <li><svg viewBox="0 0 16 16"><path d="M4 0h8a1 1 0 0 1 1 1v14a1 1 0 0 1-1 1H4a1 1 0 0 1-1-1V1a1 1 0 0 1 1-1zm1 2v10h6V2zm3 11a1 1 0 1 0 0 2 1 1 0 0 0 0-2z"/></svg>212 408 36 19</li>
    <li><svg viewBox="0 0 16 16"><path d="M4 1h8v4H4zM1 6h14v7h-3v2H4v-2H1zm4 5v3h6v-3z"/></svg>212 408 36 20</li>
    <li><svg viewBox="0 0 16 16"><path d="M1 3h14v10H1zm1 1.2V12h12V4.2L8 8.6z"/></svg>melridge@vantoreqrealty.com</li>
  </ul>
  <svg class="front-bands" viewBox="0 0 640 44" preserveAspectRatio="none" aria-hidden="true">
    <polygon points="0,44 0,30 470,0 640,0 640,44" fill="var(--teal)"/>
    <polygon points="470,0 640,0 640,44 455,44" fill="var(--band-grey)"/>
    <polygon points="466,0 472,0 457,44 451,44" fill="var(--paper)"/>
  </svg>
</section>

</body>
</html>
```